Messianic Prophetic Timeline

I would like to create a timeline that will fit on a horizontal 11 x 8 1/2 (8 1/2 x11) sheet of paper.
I have two images that will need to be merged.
There should be 7 time points. 1) 457BCE-26 AD, 2) 26 AD-30AD, 3) 30 AD-66 AD, 4) 66AD- 70AD 5) 70 AD, 6) 70AD-20??, and 7) Future
The #6 and #7 from each graphic should be merged. The 30AD-70AD can be dropped. Time point #7 Future has two different texts both need to be preserved, I would like time point #7 to be larger than the other time points.
There are scripture verses that are associated with each block that should be preserved and be more prominent.
These images are from a powerpoint slide, but I want something that can be printed out.
I run a website www.brightfieldlamp.org. I have some brand colors that if can be incorporated or at least have some color cohesion would be great, but that is not as important as readability.
Background images are nice - The idea is one of conflict between light and darkness, two opposing forces, Christ and anti-Christ. Maybe a king on a white horse battling a large serpent dragon
If you can incorporate this quote near timeblock #1-2 "From the decree to restore Jerusalem until Messiah 483 year"
Second quote anywhere "He will make a covenant with many for 7 years"

```html
<!DOCTYPE html>
<html lang="en">
<head>
<meta charset="utf-8">
<title>Jesus and Daniel Chronology</title>
<link rel="stylesheet" href="https://fonts.googleapis.com/css2?family=Bebas+Neue&family=Roboto+Condensed:wght@400;700&family=Roboto:ital,wght@0,400;0,500;0,700;1,500&display=swap">
<style>
  :root {
    --stage: #808186;
    --teal: #169b93;
    --teal-bright: #14b0a8;
    --teal-deep: #0d3f3c;
    --ink-dark: #0a2423;
    --label: #124a45;
    --title-accent: #a9dcd8;
    --card-top: #e3f3f2;
    --card-body: #ffffff;
    --card-ref: #cfe9e7;
    --heading: #17968c;
    --ref-text: #10504a;
    --body-text: #2d2d2d;
    --white: #ffffff;
  }
  * { box-sizing: border-box; margin: 0; padding: 0; }
  html, body { width: 1200px; height: 988px; overflow: hidden; background: var(--stage); }
  .sheet {
    position: absolute; left: 100px; top: 107px; width: 1001px; height: 774px;
    background: linear-gradient(100deg, var(--teal) 0%, var(--teal) 45%, #127a74 70%, var(--ink-dark) 100%);
    overflow: hidden; font-family: "Roboto", sans-serif;
  }
  .backdrop { position: absolute; inset: 0;
    background: radial-gradient(ellipse at 40% 35%, rgba(255,255,255,0.08), transparent 55%),
                radial-gradient(ellipse at 70% 70%, rgba(0,0,0,0.18), transparent 60%); }
  .masthead { position: absolute; left: 280px; top: 0; width: 441px; height: 96px; }
  .brand { position: absolute; left: 0; right: 0; top: 26px; display: flex; justify-content: center; align-items: center; gap: 10px;
    font-family: "Roboto", sans-serif; font-weight: 500; font-size: 28px; color: var(--white); letter-spacing: 1px; }
  .brand-dot { width: 14px; height: 14px; border-radius: 50%; background: var(--white); }
  .title { position: absolute; left: 0; right: 0; top: 154px; text-align: center; font-weight: 400;
    font-family: "Bebas Neue", sans-serif; font-size: 78px; line-height: 1; color: var(--white); letter-spacing: 0.5px; }
  .title .accent { color: var(--title-accent); }
  .band { position: absolute; left: 0; top: 501px; width: 1001px; height: 52px; }
  .card { position: absolute; top: 280px; width: 122px; height: 211px; border-radius: 9px;
    background: var(--card-top); text-align: center; }
  .card::after { content: ""; position: absolute; left: 50%; bottom: -13px; margin-left: -14px;
    border-left: 14px solid transparent; border-right: 14px solid transparent; border-top: 14px solid var(--card-ref); }
  .card-heading { position: absolute; left: -4px; right: -4px; top: 24px; font-family: "Roboto Condensed", sans-serif;
    font-weight: 700; font-size: 25px; color: var(--heading); line-height: 1; letter-spacing: -0.3px; white-space: nowrap; }
  .card-body { position: absolute; left: 0; right: 0; top: 75px; height: 90px; background: var(--card-body);
    font-size: 11.8px; line-height: 15.4px; color: var(--body-text); padding: 18px 4px 0; }
  .card-label { position: absolute; left: 50%; top: 58px; transform: translateX(-50%); z-index: 2; white-space: nowrap;
    background: var(--label); color: var(--white); border-radius: 3px; padding: 0 5px;
    font-family: "Roboto Condensed", sans-serif; font-weight: 700; font-size: 17px; line-height: 23px; }
  .card-ref { position: absolute; left: 0; right: 0; top: 165px; height: 46px; background: var(--card-ref);
    border-radius: 0 0 9px 9px; font-weight: 700; font-size: 12px; line-height: 16px; color: var(--ref-text);
    display: flex; flex-direction: column; justify-content: center; white-space: nowrap; }
  .card--future { background: linear-gradient(135deg, #1bbcb3, #2ab2aa); }
  .card--future .card-heading { color: var(--white); }
  .card--future .card-ref { background: #4fb9b2; color: var(--white); font-size: 10px; line-height: 13px; }
  .card--future::after { border-top-color: #4fb9b2; }
  .card-body strong { display: block; margin-top: 5px; color: #222; }
  .date { position: absolute; top: 556px; width: 122px; text-align: center; font-family: "Roboto Condensed", sans-serif;
    font-weight: 700; font-size: 16px; color: var(--white); white-space: nowrap; }
  .quote { position: absolute; font-style: italic; font-weight: 500; color: var(--white); text-align: center; white-space: nowrap; }
  .quote--decree { left: 37px; top: 590px; width: 216px; height: 80px; padding-top: 7px; font-size: 16px; line-height: 20px;
    background: linear-gradient(90deg, rgba(255,255,255,0.05), rgba(20,176,168,0.6), rgba(255,255,255,0.05)); }
  .quote--covenant { left: 360px; top: 603px; width: 480px; height: 50px; line-height: 50px; font-size: 17px;
    background: linear-gradient(90deg, transparent, rgba(20,190,180,0.75) 40%, transparent); }
  .site { position: absolute; left: 0; right: 0; top: 700px; text-align: center; font-size: 23px; letter-spacing: 3.2px; color: var(--white); }
</style>
</head>
<body>
<main class="sheet">
  <div class="backdrop" role="img" aria-label="Background artwork area in deep teal tones"></div>

  <header class="masthead">
    <svg width="441" height="96" viewBox="0 0 441 96">
      <path d="M0 0 L22 57 Q30 94 72 94 L369 94 Q411 94 419 57 L441 0" fill="var(--teal)" stroke="var(--white)" stroke-width="3"/>
    </svg>
    <div class="brand"><span class="brand-dot"></span>Brightfield</div>
  </header>

  <h1 class="title">Jesus and Daniel <span class="accent">Chronology</span></h1>

  <svg class="band" viewBox="0 0 1001 52" aria-hidden="true">
    <rect width="1001" height="52" fill="#1a8a83"/>
    <rect width="1001" height="26" fill="#21a39b"/>
    <polygon points="0,0 155,0 171,26 155,52 0,52" fill="#b6ddd9"/>
    <polygon points="138,0 290,0 306,26 290,52 138,52 154,26" fill="#8fcdc7" opacity=".9"/>
    <polygon points="275,0 425,0 441,26 425,52 275,52 291,26" fill="#5ebdb5" opacity=".8"/>
    <polygon points="410,0 560,0 576,26 560,52 410,52 426,26" fill="#2fb0a8" opacity=".8"/>
    <polygon points="545,0 695,0 711,26 695,52 545,52 561,26" fill="#14a69e" opacity=".8"/>
    <polygon points="680,0 850,0 866,26 850,52 680,52 696,26" fill="#13928b" opacity=".8"/>
    <polygon points="835,0 1001,0 1001,52 835,52 851,26" fill="#157a74" opacity=".8"/>
    <rect y="26" width="1001" height="26" fill="#000" opacity=".12"/>
    <g id="ring">
      <ellipse cx="82" cy="34" rx="26" ry="11" fill="#0c5b55" opacity=".6"/>
      <path d="M56 24 v12 a26 11 0 0 0 52 0 v-12" fill="#0f8a62"/>
      <ellipse cx="82" cy="24" rx="26" ry="11" fill="#22b3a8"/>
      <ellipse cx="82" cy="23" rx="14" ry="5" fill="#0e7d74"/>
    </g>
    <use href="#ring" x="138"/><use href="#ring" x="276"/><use href="#ring" x="414"/>
    <use href="#ring" x="552"/><use href="#ring" x="690"/><use href="#ring" x="828"/>
  </svg>

  <article class="card" style="left:21px">
    <h2 class="card-heading">Mesiah</h2><span class="card-label">Cut Off</span>
    <p class="card-body" style="padding-top:20px">438 Years<br>From Decree</p>
    <p class="card-ref">Dan 9:26 Ezra 7,9:9</p>
  </article>
  <article class="card" style="left:159px">
    <h2 class="card-heading">Covenant</h2><span class="card-label">Made</span>
    <p class="card-body" style="padding-top:20px">Jesus Make<br>Covenant with<br>many, stops<br>Sacrifice</p>
    <p class="card-ref">Dan 9:27</p>
  </article>
  <article class="card" style="left:297px">
    <h2 class="card-heading">Apostles</h2><span class="card-label">Persecution</span>
    <p class="card-body" style="padding-top:24px">In Synagogue By<br>family, friends<br>By Kings</p>
    <p class="card-ref">Luke 21:12-19</p>
  </article>
  <article class="card" style="left:435px">
    <h2 class="card-heading">Vengeance</h2><span class="card-label">Days of</span>
    <p class="card-body" style="padding-top:27px">Jerusalem<br>Surrounded Flee</p>
    <p class="card-ref">Luke 21:20-23</p>
  </article>
  <article class="card" style="left:573px">
    <h2 class="card-heading">Jerusalem</h2><span class="card-label">Desolation</span>
    <p class="card-body" style="padding-top:27px">Dispersed In<br>Nations</p>
    <p class="card-ref">Luke 21:24<br>Is 61:2&nbsp;&nbsp;&nbsp; Hos 9:7</p>
  </article>
  <article class="card" style="left:711px">
    <h2 class="card-heading">Gentiles</h2><span class="card-label">Time of</span>
    <p class="card-body" style="padding-top:27px">Trample<br>Jerusalem</p>
    <p class="card-ref">Lk 21:8-11,24<br>Mat 24:4-14</p>
  </article>
  <article class="card card--future" style="left:849px">
    <h2 class="card-heading">Covenant</h2><span class="card-label">Made</span>
    <p class="card-body" style="padding-top:13px">Stops Sacrifice<br>Causes<strong>Abomination of<br>Desolation</strong></p>
    <p class="card-ref">Luke 21:25+ Matt 24:15<br>Dan 9:27, 11:31, 12:11</p>
  </article>

  <span class="date" style="left:17px">457 BCE - 26 AD</span>
  <span class="date" style="left:148px">26 AD - 30AD</span>
  <span class="date" style="left:285px">30 AD - 66 AD</span>
  <span class="date" style="left:437px">66 AD - 70 AD</span>
  <span class="date" style="left:573px">70 AD</span>
  <span class="date" style="left:711px">70 AD - 20??</span>
  <span class="date" style="left:849px">FUTURE</span>

  <p class="quote quote--decree">From the decree to<br>restore Jerusalem until<br>Messiah 483 year</p>
  <p class="quote quote--covenant">He will make a covenant with many for 7 years</p>

  <p class="site">www.brightfieldlamp.org</p>
</main>
</body>
</html>
```